Creative Web design for Tattoo Artist

I am a tattoo artist with a private tattoo/art studio in Spring, TX. I need to design a website for my studio, to include the following "pages" :
-home/about
-FAQ
-Gallery
-Inquiries
-shop
We would like to see designs that are more dark or "moody", and like the colors black/gold.
I'd like my website to reflect my studio, an award winning private, upscale custom only tattoo studio.

I've attached some examples of styles we liked.

Target Market(s)

adults ages 18-50, interested in tattoos, or fine art

Industry/Entity Type

Tattoos/Fine Art/Arts

Coding

Coded - Design and coding required

Number of Pages Required

5+ page

Colors

Designer to choose colors to be used in the design.

Requirements
Must have
• gallery section, and e-commerce page set up so I can begin selling merchandise, I'd like the fonts to flow with my logo design

```html
<!DOCTYPE html>
<html lang="en">
<head>
<meta charset="utf-8">
<title>The Gilded Viper — Custom Tattoo Studio</title>
<link href="https://fonts.googleapis.com/css2?family=Pathway+Gothic+One&family=Montserrat:wght@400;500;600&display=swap" rel="stylesheet">
<style>
:root{
  --gold:#e3c46e;
  --gold-deep:#d8b65c;
  --ink:#1d1d1d;
  --panel:#333333;
  --card:#3a3a3a;
  --black:#0b0b0b;
  --text:#ffffff;
  --line:#6a6a6a;
}
*{margin:0;padding:0;box-sizing:border-box}
html,body{width:1200px;height:4412px;overflow:hidden;background:var(--ink)}
body{position:relative;font-family:'Montserrat',sans-serif;color:var(--text)}
.abs{position:absolute}
.display{font-family:'Pathway Gothic One',sans-serif;font-weight:400}
.heading{font-family:'Pathway Gothic One',sans-serif;font-weight:400;color:var(--gold);font-size:40px;text-align:center;left:0;width:1200px}
.copy{font-size:15px;line-height:27px;text-align:center;color:var(--text)}
.btn{display:flex;align-items:center;justify-content:center;background:var(--gold-deep);color:#222;font-family:'Pathway Gothic One',sans-serif;font-size:18px;height:38px;width:108px}
.photo{display:block}

/* hero */
.hero{left:0;top:0;width:1200px;height:625px;background:radial-gradient(ellipse at 55% 45%,#4a4a48 0%,#262625 45%,#141414 100%)}
.brand{left:150px;top:40px;font-family:'Pathway Gothic One',sans-serif;color:var(--gold);font-size:24px;line-height:26px;display:flex;align-items:center;gap:10px}
.brand i{display:block;width:12px;height:12px;border-radius:50%;background:var(--gold)}
.nav-link{position:absolute;top:50px;font-size:14px;color:#fff;text-decoration:none}
.cart{left:912px;top:48px}
.cta-top{left:967px;top:37px;width:108px;height:40px;font-size:17px}

/* about */
.about{left:0;top:625px;width:1200px;height:397px;background:linear-gradient(90deg,#2e2e2e 0%,#151515 25%,#0d0d0d 60%,#111 100%)}

/* products */
.card{width:228px;height:268px;top:1174px;background:var(--card)}
.card .photo{height:187px}
.card .label{position:absolute;left:20px;top:202px;font-family:'Pathway Gothic One',sans-serif;color:var(--gold);font-size:17px}
.card .sub{position:absolute;left:20px;top:226px;font-size:15px}
.card .price{position:absolute;right:12px;top:212px;font-size:19px;font-weight:600}

/* faq */
.faq{left:157px;width:877px;background:var(--panel)}
.faq .q{position:absolute;left:27px;font-family:'Pathway Gothic One',sans-serif;color:var(--gold);font-size:21px}
.faq .a{position:absolute;left:27px;top:56px;width:760px;font-size:14px;line-height:24px}
.faq svg{position:absolute;right:36px}

/* gallery */
.tile{position:absolute}

/* custom band */
.band{left:0;top:3250px;width:1200px;height:176px;background:linear-gradient(90deg,#050505 0%,#222 30%,#3a3a3a 45%,#0a0a0a 58%,#000 100%)}

/* inquiry */
.inquiry{left:0;top:3426px;width:1200px;height:508px;background:radial-gradient(ellipse at 60% 50%,#3b3a38 0%,#2a2927 55%,#1e1e1d 100%)}
.field{position:absolute;border-bottom:1px solid var(--line);font-size:14px;padding-left:10px;padding-bottom:18px;color:#fff}
.info{position:absolute;left:150px;font-size:14px;line-height:24px;display:flex;align-items:flex-start;gap:14px}
.info svg{margin-top:5px;flex:none}

/* footer */
.footer{left:0;top:3934px;width:1200px;height:478px;background:var(--ink)}
.rule{height:12px;background:var(--gold-deep);top:4022px}
.fcol{position:absolute;text-align:center;font-size:15px;line-height:24px}
.fcol b{display:block;font-family:'Pathway Gothic One',sans-serif;font-weight:400;color:var(--gold);font-size:19px}
.foot-link{position:absolute;top:4290px;font-size:16px;color:#fff;text-decoration:none}
.social{position:absolute;top:4298px;width:20px;height:20px;border-radius:50%;background:#fff}
</style>
</head>
<body>

<!-- hero -->
<section class="abs hero" role="img" aria-label="Dark photograph of a tattoo artist working on a serpent tattoo"></section>
<div class="abs brand"><i></i>The Gilded Viper</div>
<nav>
  <a class="nav-link" href="#" style="left:436px">About Us</a>
  <a class="nav-link" href="#" style="left:549px">FAQ</a>
  <a class="nav-link" href="#" style="left:630px">Gallery</a>
  <a class="nav-link" href="#" style="left:728px">Inquiries</a>
  <a class="nav-link" href="#" style="left:837px">Shop</a>
</nav>
<svg class="abs cart" width="22" height="20" viewBox="0 0 22 20"><path d="M1 2h3l3 10h10l3-7H6" fill="none" stroke="#fff" stroke-width="2"/><circle cx="9" cy="16" r="2" fill="#fff"/><circle cx="16" cy="16" r="2" fill="#fff"/><circle cx="19" cy="3" r="3" fill="var(--gold)"/></svg>
<div class="abs btn cta-top">Custom Tattoo</div>
<div class="abs display" style="left:0;width:1200px;top:292px;text-align:center;font-size:26px">Welcome to</div>
<div class="abs display" style="left:0;width:1200px;top:318px;text-align:center;font-size:68px;color:var(--gold)">The Gilded Viper</div>
<p class="abs copy" style="left:350px;width:500px;top:406px">Lorem ipsum dolor sit amet, consectetur adipiscing elit, sed do eiusmod tempor incididunt ut labore et dolore magna aliqua.</p>
<div class="abs btn" style="left:545px;top:477px">Get Started</div>

<!-- about -->
<section class="abs about"><div class="abs" role="img" aria-label="Gloved hand holding a tattoo machine" style="left:0;top:0;width:330px;height:397px;background:linear-gradient(135deg,#4a4a4a,#1b1b1b 70%)"></div></section>
<h2 class="abs heading" style="top:690px">About Us</h2>
<p class="abs copy" style="left:140px;width:920px;top:763px">Lorem ipsum dolor sit amet, consectetur adipiscing elit, sed do eiusmod tempor incididunt ut labore et dolore magna aliqua. Quis ipsum suspendisse ultrices gravida. Risus commodo viverra maecenas accumsan lacus vel facilisis. Lorem ipsum dolor sit amet, consectetur adipiscing elit, sed do eiusmod tempor incididunt ut labore et dolore magna aliqua. Quis ipsum suspendisse ultrices gravida. Risus commodo viverra maecenas accumsan lacus vel facilisis.</p>
<div class="abs btn" style="left:545px;top:898px">Read More</div>

<!-- products -->
<h2 class="abs heading" style="top:1087px">Our Products</h2>
<div class="abs card" style="left:130px"><div class="photo" role="img" aria-label="Skull with helmet and wings illustration" style="background:radial-gradient(circle,#c9a26a 0%,#4a3c33 70%)"></div><span class="label">Tattoo Products</span><span class="sub">Lorem Ipsum</span><span class="price">$53.34</span></div>
<div class="abs card" style="left:372px"><div class="photo" role="img" aria-label="Black and white illustration of two women in profile" style="background:linear-gradient(135deg,#eee,#bbb)"></div><span class="label">Tattoo Products</span><span class="sub">Lorem Ipsum</span><span class="price">$53.34</span></div>
<div class="abs card" style="left:615px"><div class="photo" role="img" aria-label="Skull with crossed tattoo machines illustration" style="background:radial-gradient(circle,#8a8a8a 0%,#000 60%)"></div><span class="label">Tattoo Products</span><span class="sub">Lorem Ipsum</span><span class="price">$53.34</span></div>
<div class="abs card" style="left:857px"><div class="photo" role="img" aria-label="Blue pinstripe ornament artwork on black" style="background:radial-gradient(circle,#1d4e7a 0%,#050a12 70%)"></div><span class="label">Tattoo Products</span><span class="sub">Lorem Ipsum</span><span class="price">$53.34</span></div>
<div class="abs btn" style="left:542px;top:1493px">View All</div>

<!-- faq -->
<h2 class="abs heading" style="top:1605px">Frequently Asked Questions</h2>
<p class="abs copy" style="left:140px;width:920px;top:1675px">Lorem ipsum dolor sit amet, consectetur adipiscing elit, sed do eiusmod tempor incididunt ut labore et dolore magna aliqua. Quis ipsum suspendisse ultrices gravida. Risus commodo viverra maecenas accumsan lacus vel facilisis.</p>
<div class="abs faq" style="top:1772px;height:134px"><span class="q" style="top:14px">Is It Hurt when applying tattoo?</span><p class="a">Lorem ipsum dolor sit amet, consectetur adipiscing elit, sed do eiusmod tempor incididunt ut labore et dolore magna aliqua. Quis ipsum suspendisse ultrices gravida.</p><svg style="top:24px" width="20" height="12" viewBox="0 0 20 12"><path d="M2 2l8 8 8-8" fill="none" stroke="#fff" stroke-width="2.5"/></svg></div>
<div class="abs faq" style="top:1920px;height:62px"><span class="q" style="top:16px">Is It Hurt when applying tattoo?</span><svg style="top:20px" width="12" height="20" viewBox="0 0 12 20"><path d="M2 2l8 8-8 8" fill="none" stroke="#fff" stroke-width="2.5"/></svg></div>
<div class="abs faq" style="top:1994px;height:62px"><span class="q" style="top:16px">Is It Hurt when applying tattoo?</span><svg style="top:20px" width="12" height="20" viewBox="0 0 12 20"><path d="M2 2l8 8-8 8" fill="none" stroke="#fff" stroke-width="2.5"/></svg></div>
<div class="abs faq" style="top:2066px;height:62px"><span class="q" style="top:16px">Is It Hurt when applying tattoo?</span><svg style="top:20px" width="12" height="20" viewBox="0 0 12 20"><path d="M2 2l8 8-8 8" fill="none" stroke="#fff" stroke-width="2.5"/></svg></div>
<div class="abs btn" style="left:542px;top:2162px">View More</div>

<!-- gallery -->
<h2 class="abs heading" style="top:2290px">Gallery</h2>
<p class="abs copy" style="left:140px;width:920px;top:2358px">Lorem ipsum dolor sit amet, consectetur adipiscing elit, sed do eiusmod tempor incididunt ut labore et dolore magna aliqua. Quis ipsum suspendisse ultrices gravida. Risus commodo viverra maecenas accumsan lacus vel facilisis.</p>
<div class="tile" role="img" aria-label="Close-up of tattoo needle on skin" style="left:109px;top:2468px;width:231px;height:234px;background:linear-gradient(135deg,#8a5a4a,#3a2620)"></div>
<div class="tile" role="img" aria-label="Gloved hand tattooing a mandala on skin" style="left:109px;top:2728px;width:231px;height:342px;background:linear-gradient(160deg,#2a2a2a,#b08a70 60%,#ddd)"></div>
<div class="tile" role="img" aria-label="Forearm with sleeve tattoo" style="left:359px;top:2468px;width:232px;height:344px;background:linear-gradient(135deg,#eee,#a88a72 55%,#6b5444)"></div>
<div class="tile" role="img" aria-label="Gloved hands tattooing under lamp light" style="left:359px;top:2838px;width:232px;height:232px;background:radial-gradient(circle at 40% 20%,#e8c890,#5a4a3a 45%,#1a1a1a)"></div>
<div class="tile" role="img" aria-label="Tattooed back of a person in smoky light" style="left:610px;top:2468px;width:231px;height:164px;background:linear-gradient(135deg,#9aa4aa,#3a4044)"></div>
<div class="tile" role="img" aria-label="Colour tattoo being applied" style="left:610px;top:2655px;width:231px;height:234px;background:linear-gradient(135deg,#ccc,#9a4a3a 55%,#4a2a22)"></div>
<div class="tile" role="img" aria-label="Tattooed model in red top" style="left:610px;top:2906px;width:231px;height:164px;background:linear-gradient(135deg,#c8c8c8,#8a8a8a 50%,#b83a3a)"></div>
<div class="tile" role="img" aria-label="Black gloved tattoo artist at work" style="left:860px;top:2468px;width:231px;height:234px;background:linear-gradient(135deg,#2a2a2a,#6a5a50 60%,#1a1a1a)"></div>
<div class="tile" role="img" aria-label="Gloved hands working on a detailed tattoo" style="left:860px;top:2728px;width:231px;height:342px;background:linear-gradient(135deg,#3a3a3a,#7a6a5e 55%,#2a2a2a)"></div>
<div class="abs btn" style="left:545px;top:3126px">View More</div>

<!-- custom tattoo band -->
<section class="abs band"><div class="abs" role="img" aria-label="Pinstripe ornaments and tattoo artist at work" style="left:140px;top:0;width:400px;height:176px;background:linear-gradient(90deg,rgba(60,60,60,.3),rgba(120,120,120,.35) 70%,rgba(0,0,0,0))"></div></section>
<div class="abs display" style="left:597px;top:3310px;font-size:46px">Custom Tattoo Service</div>
<div class="abs btn" style="left:961px;top:3318px;width:108px;height:40px">Click Here</div>

<!-- inquiry -->
<section class="abs inquiry"></section>
<h2 class="abs display" style="left:143px;top:3480px;font-size:40px;color:var(--gold)">Inquiry</h2>
<div class="info" style="top:3575px"><svg width="12" height="16" viewBox="0 0 12 16"><path d="M6 0a6 6 0 0 0-6 6c0 4.5 6 10 6 10s6-5.5 6-10a6 6 0 0 0-6-6z" fill="#fff"/><circle cx="6" cy="6" r="2.2" fill="#2a2927"/></svg><span>24, Cedar Hollow Lane, Oak<br>Ridge USA -77390.</span></div>
<div class="info" style="top:3683px"><svg width="14" height="14" viewBox="0 0 24 24"><path d="M6.6 10.8a15 15 0 0 0 6.6 6.6l2.2-2.2a1 1 0 0 1 1-.25 11.4 11.4 0 0 0 3.6.6 1 1 0 0 1 1 1V20a1 1 0 0 1-1 1A17 17 0 0 1 3 4a1 1 0 0 1 1-1h3.5a1 1 0 0 1 1 1c0 1.25.2 2.45.6 3.6a1 1 0 0 1-.25 1z" fill="#fff"/></svg><span>(+1) 555 014 2290</span></div>
<div class="info" style="top:3784px"><svg width="14" height="14" viewBox="0 0 14 14"><circle cx="7" cy="7" r="6" fill="none" stroke="#fff" stroke-width="1.4"/><path d="M7 3.5V7l2.5 1.5" fill="none" stroke="#fff" stroke-width="1.4"/></svg><span>Monday - Friday<br>9:00 AM to 10:00 PM</span></div>
<div class="field" style="left:550px;top:3520px;width:229px">First Name</div>
<div class="field" style="left:818px;top:3520px;width:229px">Last Name</div>
<div class="field" style="left:550px;top:3623px;width:229px">Phone Number</div>
<div class="field" style="left:818px;top:3623px;width:229px">Email</div>
<div class="field" style="left:550px;top:3743px;width:497px">Message</div>
<div class="abs btn" style="left:745px;top:3818px">Submit</div>

<!-- footer -->
<section class="abs footer"></section>
<div class="abs rule" style="left:0;width:524px"></div>
<div class="abs rule" style="left:668px;width:532px"></div>
<div class="abs display" style="left:524px;width:144px;top:4004px;text-align:center;font-size:22px;line-height:24px;color:var(--gold)">The Gilded<br>Viper</div>
<div class="fcol" style="left:100px;width:270px;top:4160px"><b>Address</b>24, Cedar Hollow Lane, Oak<br>Ridge USA -77390.</div>
<div class="fcol" style="left:468px;width:270px;top:4160px"><b>Phone</b>(+1) 555 014 2290</div>
<div class="fcol" style="left:852px;width:270px;top:4163px"><b>Timing</b>Monday - Friday<br>9:00 AM to 10:00 PM</div>
<nav>
  <a class="foot-link" href="#" style="left:157px">About Us</a>
  <a class="foot-link" href="#" style="left:285px">FAQ</a>
  <a class="foot-link" href="#" style="left:376px">Gallery</a>
  <a class="foot-link" href="#" style="left:486px">Inquiries</a>
  <a class="foot-link" href="#" style="left:609px">Shop</a>
</nav>
<div aria-label="Social links">
  <span class="social" style="left:900px"></span>
  <span class="social" style="left:950px"></span>
  <span class="social" style="left:1001px"></span>
  <span class="social" style="left:1051px"></span>
</div>
<div class="abs" style="left:0;top:4352px;width:1200px;height:1px;background:#444"></div>
<div class="abs" style="left:0;width:1200px;top:4372px;text-align:center;font-size:12px">© copyrights 2023 The Gilded Viper | All Rights Reserved</div>

</body>
</html>
```